Banner Project for website

We do not like our current banner and need this updated. Our website is:
https://inkvelmo.com/
We need the banner to have the following wording on the left side:
See attachment. (screenshot text on the left)
On the right side, I want to replace the lady and have a nice image of printed products like the following websites which have an image with different printed prodcuts bundled together or seperately.
https://www.labelwharf.com/
https://boxtiderun.com/
The banner must look fresh and vibrant
Target Market(s)
Small businesses
Industry/Entity Type
Printing
Requirements
Must have
- Greta banner image

```html
<!DOCTYPE html>
<html lang="en">
<head>
<meta charset="UTF-8">
<title>Compare Quotes and Save – Inkvelmo</title>
<link rel="stylesheet" href="https://fonts.googleapis.com/css2?family=Fraunces:opsz,wght@9..144,700;9..144,800&family=Roboto:wght@400;700&display=swap">
<style>
  :root {
    --brand-blue: #1b5898;
    --title-blue: #d3e5fa;
    --pill-blue: #86b2df;
    --text-white: #ffffff;
    --cards-tone: #c9c0bd;
    --cards-tone-2: #e9b9bd;
    --flyer-tone: #dcd2c2;
    --flyer-tone-2: #b7aea3;
    --brochure-tone: #2d8ad8;
    --brochure-tone-2: #1b67b3;
    --poster-tone: #e8245a;
    --poster-tone-2: #f25b83;
  }
  * { margin: 0; padding: 0; box-sizing: border-box; }
  html, body {
    width: 1200px;
    height: 462px;
    overflow: hidden;
    background: var(--brand-blue);
  }
  .banner {
    position: relative;
    width: 1200px;
    height: 462px;
    background: var(--brand-blue);
    overflow: hidden;
    font-family: "Roboto", Arial, sans-serif;
  }
  .product-collage {
    position: absolute;
    inset: 0;
    width: 1200px;
    height: 462px;
  }
  .banner-copy {
    position: absolute;
    left: 86px;
    top: 12px;
    width: 640px;
  }
  .headline {
    font-family: "Fraunces", Georgia, serif;
    font-weight: 800;
    font-size: 62px;
    line-height: 72px;
    color: var(--title-blue);
    letter-spacing: -0.5px;
    white-space: nowrap;
  }
  .intro {
    margin-top: 12px;
    font-size: 21px;
    line-height: 21px;
    color: var(--text-white);
    white-space: nowrap;
  }
  .intro + .intro { margin-top: 16px; }
  .quote-form {
    position: absolute;
    left: 86px;
    top: 272px;
    width: 400px;
    display: flex;
    flex-direction: column;
    gap: 13px;
  }
  .pill {
    height: 46px;
    border-radius: 23px;
    background: var(--pill-blue);
    color: var(--text-white);
    font-weight: 700;
    font-size: 19px;
    display: flex;
    align-items: center;
    justify-content: center;
  }
</style>
</head>
<body>
  <div class="banner">
    <svg class="product-collage" viewBox="0 0 780 300" preserveAspectRatio="none" xmlns="http://www.w3.org/2000/svg">
      <defs>
        <linearGradient id="cardsFill" x1="0" y1="0" x2="1" y2="1">
          <stop offset="0" stop-color="var(--cards-tone)"/>
          <stop offset="1" stop-color="var(--cards-tone-2)"/>
        </linearGradient>
        <linearGradient id="flyerFill" x1="0" y1="0" x2="0" y2="1">
          <stop offset="0" stop-color="var(--flyer-tone)"/>
          <stop offset="1" stop-color="var(--flyer-tone-2)"/>
        </linearGradient>
        <linearGradient id="brochureFill" x1="0" y1="0" x2="1" y2="1">
          <stop offset="0" stop-color="var(--brochure-tone-2)"/>
          <stop offset="1" stop-color="var(--brochure-tone)"/>
        </linearGradient>
        <linearGradient id="posterFill" x1="0" y1="0" x2="1" y2="0">
          <stop offset="0" stop-color="var(--poster-tone)"/>
          <stop offset="1" stop-color="var(--poster-tone-2)"/>
        </linearGradient>
      </defs>
      <polygon class="panel-cards" role="img" aria-label="Photo of printed business cards in grey and pink" points="448,0 706,0 646,102 556,78 472,58" fill="url(#cardsFill)"/>
      <polygon class="panel-flyer" role="img" aria-label="Photo of a hand holding a printed promotional flyer" points="412,74 566,118 548,262 482,300 424,300" fill="url(#flyerFill)"/>
      <polygon class="panel-brochure" role="img" aria-label="Photo of an open tri-fold blue brochure" points="716,22 780,8 780,228 562,232 598,142" fill="url(#brochureFill)"/>
      <polygon class="panel-poster" role="img" aria-label="Photo of bold red printed posters" points="496,300 522,256 780,238 780,300" fill="url(#posterFill)"/>
    </svg>

    <div class="banner-copy">
      <h1 class="headline">Compare Quotes<br>and Save</h1>
      <p class="intro">Get intants quotes, compare products from multiple<br>printers and get best price.</p>
      <p class="intro">Easy online ordering and free design.</p>
    </div>

    <div class="quote-form">
      <div class="pill pill-category">What do you want to print today?</div>
      <div class="pill pill-subcategory">Sub Category</div>
      <div class="pill pill-submit">GET QUOTES</div>
    </div>
  </div>
</body>
</html>
```